THE MAPLE BARN WEBSITE for Physio, Fitness, health

An attractive website advertising a physiotherapyand fitness / gym business, not generic, colours are natural, greens, browns, beiges. No cheesy pictures. With the ability to sell a small,amount of goods online if i decide to. Simple to navigate. Text boxes that i can input the main information and change easily. Somewhere to put my timetable. Easy to find contact details. However many pages it needs, im not fussed.
Target Market(s)
People looking for rehabilitation or fitness classes
Industry/Entity Type
Physiotherapy, Fitness, Gym, Health
Coding
Coded - Design and coding required
Number of Pages Required
1 page
Font styles to use
Other font styles liked:
- Im not fusse,ld, not script
Requirements
Must have
- Will upload posts from my business insta page for reference about the feel. Earthy natural tones, I have a lot of timber, and rustic looking piece's, plants etc in my clinic
Nice to have
- Simple to navigate
Should not have
- Cheesy "yoga" or generic "people doing physio" pics

```html
<!DOCTYPE html>
<html lang="en">
<head>
<meta charset="utf-8">
<title>The Maple Barn — Physio &amp; Fitness</title>
<link href="https://fonts.googleapis.com/css2?family=Big+Shoulders+Display:wght@200;400;500;700;800&family=Jost:ital,wght@0,400;0,500;1,400&display=swap" rel="stylesheet">
<style>
:root{
  --green:#2d4f1f;
  --green-dark:#1f3814;
  --green-soft:#8fa07f;
  --ink:#1c1c1c;
  --muted:#5a5a5a;
  --white:#ffffff;
}
*{margin:0;padding:0;box-sizing:border-box}
html,body{width:1200px;height:4004px;overflow:hidden;background:var(--white)}
body{position:relative;font-family:'Jost',sans-serif;color:var(--ink)}
.abs{position:absolute}
.display{font-family:'Big Shoulders Display',sans-serif;text-transform:uppercase}

/* hero */
.hero{left:0;top:0;width:1200px;height:768px;background:var(--green);border-radius:0 0 18px 18px;overflow:hidden}
.hero-photo{left:681px;top:0;width:519px;height:768px;background:radial-gradient(circle at 40% 40%,#3a3a3a 0%,#181818 55%,#0a0a0a 100%)}
.hero-figure{left:520px;top:140px;width:340px;height:628px;background:linear-gradient(180deg,#d8b8a4 0%,#c9a28a 40%,#2a2a2a 85%);border-radius:170px 170px 0 0;opacity:.9}
.brand{color:var(--white);font-family:'Big Shoulders Display',sans-serif;font-weight:800;text-transform:uppercase;line-height:1;text-align:center}
.brand-top{left:100px;top:28px;width:136px;font-size:26px;letter-spacing:1px}
.nav{top:50px;font-family:'Big Shoulders Display',sans-serif;font-size:19px;color:var(--white);font-weight:500}
.nav-active{border-bottom:2px solid var(--white);padding-bottom:4px}
.btn-contact{left:964px;top:36px;width:146px;height:50px;border-radius:25px;background:var(--green);color:var(--white);font-family:'Big Shoulders Display',sans-serif;font-weight:500;font-size:19px;display:flex;align-items:center;justify-content:center}
.hero-title{left:86px;top:226px;font-size:96px;font-weight:800;color:var(--white);line-height:1}
.hero-title-thin{left:84px;top:320px;font-size:114px;font-weight:200;color:var(--white);line-height:1}
.hero-sub{left:90px;top:442px;font-size:14px;color:var(--white)}
.btn-light{background:var(--white);color:var(--ink);font-family:'Big Shoulders Display',sans-serif;font-weight:500;border-radius:24px;display:flex;align-items:center;justify-content:center;font-size:19px}
.slider-bar{left:797px;top:662px;width:403px;height:59px;background:var(--green);border-radius:30px 0 0 30px}
.slider-count{left:948px;top:677px;color:var(--white);font-family:'Big Shoulders Display',sans-serif;font-weight:500;font-size:19px}
.slider-dot{width:46px;height:46px;border-radius:50%;top:668px;display:flex;align-items:center;justify-content:center}

/* about */
.about-photo{left:146px;top:866px;width:410px;height:410px;border-radius:50%;background:radial-gradient(circle at 40% 45%,#5a6446 0%,#9a9a94 45%,#c8c8c4 100%)}
.eyebrow{font-family:'Big Shoulders Display',sans-serif;font-weight:500;font-size:19px;color:var(--green);text-transform:uppercase}
.h2{font-family:'Big Shoulders Display',sans-serif;font-weight:800;text-transform:uppercase;font-size:48px;line-height:1.05;color:var(--ink)}
.body-copy{font-size:13.5px;line-height:19.5px;color:var(--muted)}
.btn-green{background:var(--green-dark);color:var(--white);font-family:'Big Shoulders Display',sans-serif;font-weight:500;border-radius:22px;display:flex;align-items:center;justify-content:center;font-size:19px}

/* schedule */
.center{left:0;width:1200px;text-align:center}
.services-band{left:0;top:1728px;width:1200px;height:836px;background:var(--green);border-radius:20px}
.video{left:89px;top:1489px;width:1021px;height:468px;border-radius:14px;background:linear-gradient(180deg,#262626 0%,#4a3a2a 45%,#2a2a2a 75%,#3a3a3a 100%)}
.play{left:530px;top:1660px;width:136px;height:136px;border-radius:50%;background:rgba(255,255,255,.25);display:flex;align-items:center;justify-content:center}

/* services */
.svc-eyebrow{left:110px;top:2043px;font-family:'Big Shoulders Display',sans-serif;font-weight:500;font-size:19px;color:var(--white)}
.svc-title{left:110px;top:2078px;font-size:46px;font-weight:800;color:var(--white)}
.svc-rule{left:110px;top:2139px;width:53px;height:3px;background:var(--white)}
.svc-item{left:110px;width:560px;height:70px;display:flex;align-items:center}
.svc-icon{width:70px;height:70px;border-radius:50%;background:var(--white);display:flex;align-items:center;justify-content:center;flex:none}
.svc-text{margin-left:12px;color:var(--white)}
.svc-text h3{font-family:'Big Shoulders Display',sans-serif;font-weight:500;font-size:19px;text-transform:uppercase}
.svc-text p{font-size:13.5px;margin-top:2px}
.svc-photo{left:700px;top:2060px;width:390px;height:390px;border-radius:50%;background:radial-gradient(circle,#6f7f66 0%,#3c5a2c 70%)}
.svc-figure{left:760px;top:2020px;width:270px;height:482px;border-radius:135px 135px 40px 40px;background:linear-gradient(180deg,#b27c66 0%,#222 35%,#8a8a8a 65%,#cfcfcf 100%)}

/* shop */
.shop-tile{top:2808px;width:245px;height:213px;border-radius:10px}

/* testimonials */
.quote{font-style:italic;font-size:16px;line-height:25px;color:var(--muted)}
.dots{top:3346px;left:577px;display:flex;gap:6px}
.dots span{width:12px;height:12px;border-radius:50%;background:var(--green-soft)}
.dots span.on{background:var(--green-dark)}

/* footer */
.footer{left:0;top:3470px;width:1200px;height:534px;background:var(--green);border-radius:20px 20px 0 0}
.brand-foot{left:520px;top:3510px;width:160px;font-size:32px}
.f-head{top:3672px;font-family:'Big Shoulders Display',sans-serif;font-weight:800;font-size:24px;color:var(--white)}
.f-list{list-style:none;font-size:13px;color:var(--white)}
.f-list li{height:26.5px}
.f-row{display:flex;align-items:flex-start;gap:8px}
.f-contact{font-size:13px;line-height:16px;color:var(--white)}
.social-dot{width:14px;height:14px;border-radius:50%;background:var(--white);flex:none;margin-top:2px}
.news-input{left:732px;top:3758px;width:378px;height:57px;border-radius:29px;background:var(--white);border:3px solid var(--green-soft)}
.news-input span{position:absolute;left:24px;top:17px;font-size:14px;color:var(--ink)}
.btn-sub{position:absolute;right:4px;top:4px;width:128px;height:43px;border-radius:22px;background:var(--green-dark);color:var(--white);font-family:'Big Shoulders Display',sans-serif;font-weight:500;font-size:19px;display:flex;align-items:center;justify-content:center}
.f-rule{left:89px;top:3935px;width:1021px;height:1px;background:rgba(255,255,255,.6)}
.to-top{left:1127px;top:3909px;width:52px;height:52px;border-radius:50%;background:var(--white);border:3px solid var(--green);display:flex;align-items:center;justify-content:center}
.f-legal{top:3959px;font-size:12.5px;color:var(--white)}
</style>
</head>
<body>

<section class="abs hero">
  <div class="abs hero-photo" role="img" aria-label="Dark gym interior with weight racks"></div>
  <div class="abs hero-figure" role="img" aria-label="Athlete holding purple dumbbells"></div>
  <div class="abs brand brand-top">The Maple<br>Barn</div>
  <nav>
    <span class="abs nav nav-active" style="left:525px">HOME</span>
    <span class="abs nav" style="left:605px">ABOUT</span>
    <span class="abs nav" style="left:690px">SERVICES</span>
    <span class="abs nav" style="left:794px">TIMETABLE</span>
    <span class="abs nav" style="left:904px">SHOP</span>
    <span class="abs btn-contact">CONTACT US</span>
  </nav>
  <h1 class="abs display hero-title">Move Well.</h1>
  <div class="abs display hero-title-thin">Live Fully.</div>
  <p class="abs hero-sub">Rehabilitation &amp; fitness in a grounded, real-world setting.</p>
  <span class="abs btn-light" style="left:90px;top:483px;width:206px;height:44px">CHECK OUR TIMETABLE</span>
  <div class="abs slider-bar"></div>
  <span class="abs btn-light" style="left:797px;top:662px;width:128px;height:59px;border-radius:30px">LEARN MORE</span>
  <span class="abs slider-count">01/03</span>
  <span class="abs slider-dot" style="left:1006px;background:#5f7556"><svg width="12" height="12" viewBox="0 0 12 12"><path d="M9 1 3 6l6 5z" fill="#fff"/></svg></span>
  <span class="abs slider-dot" style="left:1063px;background:#fff"><svg width="12" height="12" viewBox="0 0 12 12"><path d="M3 1l6 5-6 5z" fill="#111"/></svg></span>
</section>

<section>
  <div class="abs about-photo" role="img" aria-label="Branded cap and t-shirt laid flat"></div>
  <div class="abs eyebrow" style="left:603px;top:922px">About Us</div>
  <h2 class="abs h2" style="left:601px;top:958px;width:470px">Rooted in nature. Backed by science.</h2>
  <p class="abs body-copy" style="left:603px;top:1066px;width:460px">We offer evidence-based physiotherapy and functional fitness solutions in a calm, welcoming space designed with timber, greenery, and natural textures. Our mission is simple — to help you move better, feel stronger, and stay active, whether you're recovering from an injury or building everyday strength.</p>
  <span class="abs btn-green" style="left:603px;top:1186px;width:131px;height:43px">READ MORE</span>
</section>

<section>
  <h2 class="abs h2 center" style="top:1358px">Weekly Class &amp; Appointment Schedule</h2>
  <p class="abs body-copy center" style="top:1418px;left:230px;width:740px;font-size:13px">Embed calendar or use a dynamic table that can be updated easily — e.g., Planner Sync integration or CMS controlled text area.</p>
  <div class="abs services-band"></div>
  <div class="abs video" role="img" aria-label="Video still of a woman training with battle ropes in the gym"></div>
  <div class="abs play"><svg width="34" height="38" viewBox="0 0 34 38"><path d="M4 2l28 17L4 36z" fill="#fff"/></svg></div>
</section>

<section>
  <div class="abs svc-eyebrow">OUR SERVICE</div>
  <h2 class="abs display svc-title">What We Offer</h2>
  <div class="abs svc-rule"></div>

  <div class="abs svc-item" style="top:2165px">
    <div class="svc-icon"><svg width="40" height="40" viewBox="0 0 40 40" fill="none" stroke="#2d4f1f" stroke-width="2"><rect x="10" y="8" width="20" height="24" rx="3"/><path d="M15 16h10M15 21h10M15 26h6"/></svg></div>
    <div class="svc-text"><h3>Physiotherapy Treatment</h3><p>Individual care tailored to your injury and goals.</p></div>
  </div>
  <div class="abs svc-item" style="top:2248px">
    <div class="svc-icon"><svg width="40" height="40" viewBox="0 0 40 40" fill="none" stroke="#2d4f1f" stroke-width="2"><path d="M12 28 28 12"/><rect x="6" y="22" width="8" height="12" rx="2" transform="rotate(-45 10 28)"/><rect x="26" y="6" width="8" height="12" rx="2" transform="rotate(-45 30 12)"/></svg></div>
    <div class="svc-text"><h3>Fitness &amp; Rehab Classes</h3><p>Small group sessions focused on strength, mobility, &amp; balance.</p></div>
  </div>
  <div class="abs svc-item" style="top:2330px">
    <div class="svc-icon"><svg width="40" height="40" viewBox="0 0 40 40" fill="none" stroke="#2d4f1f" stroke-width="2"><path d="M8 20h24"/><rect x="6" y="13" width="5" height="14" rx="1"/><rect x="29" y="13" width="5" height="14" rx="1"/><circle cx="20" cy="13" r="3"/></svg></div>
    <div class="svc-text"><h3>One-on-One Training</h3><p>Personalized movement plans with our experienced team.</p></div>
  </div>
  <div class="abs svc-item" style="top:2414px">
    <div class="svc-icon"><svg width="40" height="40" viewBox="0 0 40 40" fill="none" stroke="#2d4f1f" stroke-width="2"><circle cx="20" cy="20" r="11"/><path d="M20 13v7l5 4"/></svg></div>
    <div class="svc-text"><h3>Bodywork &amp; Recovery</h3><p>Including massage, dry needling, and movement therapy.</p></div>
  </div>

  <div class="abs svc-photo" role="img" aria-label="Dotted circle backdrop"></div>
  <div class="abs svc-figure" role="img" aria-label="Woman kneeling with a dumbbell"></div>
</section>

<section>
  <div class="abs eyebrow center" style="top:2651px">Online Store</div>
  <h2 class="abs h2 center" style="top:2684px;left:230px;width:740px;line-height:1.1">Shop Essentials (Optional Section - Can Hide If Not Selling Initially)</h2>
  <div class="abs shop-tile" style="left:89px;background:linear-gradient(160deg,#6b6b6b,#1e1e1e)" role="img" aria-label="Branded training t-shirt"></div>
  <div class="abs shop-tile" style="left:349px;background:linear-gradient(160deg,#c9c08c,#8a5a4a)" role="img" aria-label="Branded drink tumblers"></div>
  <div class="abs shop-tile" style="left:608px;background:linear-gradient(160deg,#cdb49a,#8a6a50)" role="img" aria-label="Heat pack and gift box"></div>
  <div class="abs shop-tile" style="left:866px;background:linear-gradient(160deg,#4f7a3a,#c8c8b8)" role="img" aria-label="Recovery spray bottle among leaves"></div>
</section>

<section>
  <svg class="abs" style="left:571px;top:3073px" width="58" height="40" viewBox="0 0 58 40"><path d="M2 22C2 10 10 2 22 1v8C16 10 13 14 13 18h9v20H2z M34 22C34 10 42 2 54 1v8c-6 1-9 5-9 9h9v20H34z" fill="#c8cdc4"/></svg>
  <div class="abs eyebrow center" style="top:3121px">Testimonials</div>
  <h2 class="abs h2 center" style="top:3155px">What Our Clients Say</h2>
  <p class="abs quote center" style="top:3216px;left:230px;width:740px">“I've tried gyms and rehab centres before, but nothing felt as comfortable or honest as this space. It's calm, real, and the people actually listen. I'm finally moving better without feeling overwhelmed.”</p>
  <div class="abs eyebrow center" style="top:3302px;color:var(--ink)">Hannah R</div>
  <div class="abs dots"><span></span><span class="on"></span><span></span></div>
</section>

<footer>
  <div class="abs footer"></div>
  <div class="abs brand brand-foot">The Maple<br>Barn</div>

  <h4 class="abs f-head" style="left:89px">QUICK LINKS</h4>
  <ul class="abs f-list" style="left:89px;top:3710px">
    <li>Home</li><li>About</li><li>Services</li><li>Timetable</li><li>Shop</li><li>Contact Us</li>
  </ul>

  <h4 class="abs f-head" style="left:294px">CONTACT US</h4>
  <div class="abs f-contact" style="left:294px;top:3710px;width:220px">
    <div class="f-row"><svg width="10" height="12" viewBox="0 0 10 12"><path d="M2 1l2 2-1 2c1 2 2 3 4 4l2-1 1 2-2 2C4 12 0 7 1 2z" fill="#fff"/></svg><span>Phone:<br>(555)010-2468</span></div>
    <div class="f-row" style="margin-top:12px"><svg width="10" height="10" viewBox="0 0 10 10"><rect x="0" y="2" width="10" height="7" fill="#fff"/><path d="M0 2l5 4 5-4" stroke="#2d4f1f" fill="none"/></svg><span>Email:<br>hello@maplebarn.test</span></div>
    <div class="f-row" style="margin-top:12px"><svg width="10" height="12" viewBox="0 0 10 12"><path d="M5 0a4 4 0 0 1 4 4c0 3-4 8-4 8S1 7 1 4a4 4 0 0 1 4-4z" fill="#fff"/><circle cx="5" cy="4" r="1.5" fill="#2d4f1f"/></svg><span>Address:<br>Some Address line here<br>united kingdom AB12 3CD</span></div>
  </div>

  <h4 class="abs f-head" style="left:545px">FOLLOW US</h4>
  <ul class="abs f-list" style="left:545px;top:3710px">
    <li class="f-row"><span class="social-dot"></span>Friendspace</li>
    <li class="f-row" style="margin-top:9px"><span class="social-dot"></span>Chirper</li>
    <li class="f-row" style="margin-top:9px"><span class="social-dot"></span>Chatline</li>
    <li class="f-row" style="margin-top:9px"><span class="social-dot"></span>Papergram</li>
    <li class="f-row" style="margin-top:9px"><span class="social-dot"></span>Workline</li>
  </ul>

  <h4 class="abs f-head" style="left:729px">WHAT OUR NEWSLETTER</h4>
  <p class="abs" style="left:730px;top:3725px;font-size:13px;color:#fff">Subscribe to our newsletter for the latest updates</p>
  <div class="abs news-input"><span>Your Email Here</span><div class="btn-sub">SUBSCRIBE</div></div>

  <div class="abs f-rule"></div>
  <div class="abs to-top"><svg width="12" height="8" viewBox="0 0 12 8"><path d="M1 7l5-5 5 5" stroke="#2d4f1f" stroke-width="2" fill="none"/></svg></div>
  <p class="abs f-legal" style="left:89px">Copyright © 2025 The Maple Barn. All Rights Reserved.</p>
  <p class="abs f-legal" style="left:788px">Privacy Policy &nbsp;|&nbsp; Terms of Service &nbsp;|&nbsp; Cookie Settings</p>
</footer>

</body>
</html>
```